Car Wrap Design for Solar Energy Company

We are company that sell and install solar systems and components. We have three Velmo Trask cars and one Kovini Pelder open back van. We are looking to crate a cool car design that we can use for all our vehicles now and in the future. We are looking more for a whole design, instead of separate elements. It would be nice if its, something that can work on future cars that are different than the ones now.

Target Market(s)

Domestic

Industry/Entity Type

Solar Energy

Font styles to use
Sans Serif

Colors
0054AA
0677BA
7BADD7
CADEEF
E8F1F8
59FF00
82FF00
B8FF75
E3FFCB
F4FFEA
FFF300
FFF600
FEFA6F
FFFEC7
FFFEE8
F0912C
F2A743
F7CA91
FBE8D2
FDF5EE

Requirements
Must have
• The logo, website, phone, socials

```html
<!DOCTYPE html>
<html lang="en">
<head>
<meta charset="utf-8">
<title>Helioden – Vehicle Wrap</title>
<link href="https://fonts.googleapis.com/css2?family=Montserrat:wght@500;600;700&display=swap" rel="stylesheet">
<style>
  :root {
    --sky: #52cffd;
    --navy: #1b2a3d;
    --blue: #0677ba;
    --blue-light: #7badd7;
    --blue-pale: #cadeef;
    --white: #ffffff;
    --gold: #f2a743;
  }
  html, body {
    margin: 0;
    width: 1200px;
    height: 675px;
    overflow: hidden;
    background: var(--sky);
  }
  .wrap-canvas {
    display: block;
    width: 1200px;
    height: 675px;
    font-family: "Montserrat", sans-serif;
  }
  .band-navy { fill: var(--navy); }
  .band-blue { fill: var(--blue); }
  .band-white { fill: var(--white); }
  .rule-gold { fill: var(--gold); }
  .social-label { fill: var(--white); font-weight: 700; font-size: 16px; letter-spacing: 1px; }
  .social-handle { fill: var(--white); font-weight: 600; font-size: 18px; }
  .brand-name { fill: var(--navy); font-weight: 600; font-size: 66px; letter-spacing: 2px; }
  .brand-dot { fill: var(--gold); }
  .contact-web { fill: var(--white); font-weight: 700; font-size: 26px; letter-spacing: 1px; }
  .contact-phone { fill: var(--white); font-weight: 700; font-size: 36px; letter-spacing: 1px; }
  .contact-icon { fill: none; stroke: var(--white); stroke-width: 3; stroke-linecap: round; stroke-linejoin: round; }
</style>
</head>
<body>
<svg class="wrap-canvas" viewBox="0 0 1200 675" xmlns="http://www.w3.org/2000/svg">
  <defs>
    <clipPath id="wrap-side">
      <rect x="40" y="110" width="1120" height="450" rx="40"/>
    </clipPath>
    <linearGradient id="halftone-tone" x1="0" y1="0" x2="1" y2="1">
      <stop offset="0" stop-color="#e3eef8"/>
      <stop offset="0.5" stop-color="#b9d6ee"/>
      <stop offset="1" stop-color="#9cc4e6"/>
    </linearGradient>
    <linearGradient id="panel-tone" x1="0" y1="0" x2="1" y2="1">
      <stop offset="0" stop-color="#7badd7"/>
      <stop offset="1" stop-color="#0677ba"/>
    </linearGradient>
    <radialGradient id="sun-tone" cx="0.5" cy="0.5" r="0.5">
      <stop offset="0" stop-color="#f2a743"/>
      <stop offset="1" stop-color="#f7ca91"/>
    </radialGradient>
  </defs>

  <g clip-path="url(#wrap-side)">
    <rect class="halftone-field" role="img" aria-label="Light blue halftone dot pattern" x="40" y="110" width="1120" height="450" fill="url(#halftone-tone)"/>
    <path class="sweep-blue" d="M40 560 L40 520 C200 500 360 470 520 330 L600 330 C480 470 330 540 250 560 Z" fill="var(--blue)" opacity="0.9"/>
    <path class="sweep-rule" d="M40 516 C200 496 356 466 516 326" fill="none" stroke="var(--gold)" stroke-width="3"/>
    <circle class="sun-art" role="img" aria-label="Golden sun illustration" cx="930" cy="400" r="75" fill="url(#sun-tone)"/>
    <rect class="panel-art" role="img" aria-label="Illustration of tilted blue solar panels" x="980" y="300" width="180" height="260" fill="url(#panel-tone)"/>
    <rect class="panel-art-top" role="img" aria-label="Blue solar panel graphic" x="960" y="110" width="200" height="90" fill="var(--blue)"/>

    <g class="diagonal-bands" transform="translate(700 262) rotate(-38)">
      <rect class="band-navy" x="-1000" y="-172" width="2000" height="92"/>
      <rect class="rule-gold" x="-1000" y="-80" width="2000" height="4"/>
      <rect class="band-white" x="-1000" y="-76" width="2000" height="116"/>
      <rect class="rule-gold" x="-1000" y="40" width="2000" height="4"/>
      <rect class="band-navy" x="-1000" y="44" width="2000" height="126"/>
      <rect class="band-blue" x="-1000" y="170" width="2000" height="36"/>
      <rect class="rule-gold" x="-1000" y="206" width="2000" height="3"/>

      <text class="social-label" x="-20" y="-136" text-anchor="middle">JOIN US ON:</text>
      <text class="social-handle" x="-20" y="-104" text-anchor="middle">@helioden</text>

      <circle class="brand-dot" cx="-200" cy="-40" r="13"/>
      <text class="brand-name" x="10" y="8" text-anchor="middle">HELIODEN</text>

      <g class="contact-web-row">
        <circle class="contact-icon" cx="-200" cy="90" r="13"/>
        <path class="contact-icon" d="M-213 90h26M-200 77c-7 8-7 18 0 26M-200 77c7 8 7 18 0 26"/>
        <text class="contact-web" x="-175" y="99">WWW.HELIODEN.COM</text>
      </g>
      <g class="contact-phone-row">
        <path class="contact-icon" d="M-212 122c-3 6 4 18 14 24 4 2 8 1 10-2l-6-6-5 3c-4-2-7-6-8-10l3-4-5-7c-1 0-2 1-3 2z"/>
        <text class="contact-phone" x="-175" y="150">010 2345 678</text>
      </g>
    </g>
  </g>
</svg>
</body>
</html>
```